Redesign Our Presentation on Rational Prescribing

We are looking for a new designer for QVMed, a project that creates educational modules for healthcare providers in the District of Columbia (more information at hlb.example-gov.org/qvmed). We want someone to redesign our powerpoints to look clean and professional, with original graphics that reflect the content on the slides. We also want someone who is creative and could potentially also redesign factsheets, written reports, and promotional postcards.

All the text on the slides must stay the same and it must be in the template (red line at the top, with the red box at the bottom, with the Harlow Bureau of Wellness logo). We want a powerpoint that features original graphics, looks professional, looks clean and is easy to read.

Industry/Entity Type

Healthcare

```html
<!DOCTYPE html>
<html lang="en">
<head>
<meta charset="utf-8">
<title>Medication Use in Elders – Slide Set</title>
<link href="https://fonts.googleapis.com/css2?family=Lato:wght@300;400;700&display=swap" rel="stylesheet">
<style>
:root{
  --red:#ec1c24;
  --navy:#25256b;
  --gold:#c49a3a;
  --grey-bg:#e4e4e4;
  --panel:#efeff1;
  --ring:#d6d6d6;
  --text:#4a4a4a;
  --green:#9fe0b5;
  --coral:#f06f6f;
  --sky:#8fc4ec;
}
*{box-sizing:border-box;margin:0;padding:0}
html,body{width:1200px;height:1000px;overflow:hidden}
body{background:var(--grey-bg);font-family:'Lato',sans-serif;color:var(--text);position:relative}
.slide{position:absolute;width:522px;height:294px;background:#fff;overflow:hidden}
.s-title{left:53px;top:181px}
.s-diabetes{left:624px;top:181px}
.s-antipsych{left:53px;top:524px}
.s-adr{left:624px;top:524px}

.heading{position:absolute;left:42px;top:23px;font-size:15px;font-weight:400;color:#333}
.heading-rule{position:absolute;left:30px;right:0;top:44px;height:1px;background:var(--red)}
.page-no{position:absolute;right:5px;top:7px;width:16px;height:16px;background:var(--navy);color:#fff;font-size:7px;display:flex;align-items:center;justify-content:center;border-radius:2px 4px 2px 2px}
.footer{position:absolute;left:0;right:0;bottom:0;height:17px;background:var(--red);color:#fff;font-size:6.5px;padding-left:18px;line-height:17px}
.brand{position:absolute;left:18px;bottom:22px;display:flex;align-items:center;gap:3px;font-size:6px;font-weight:700;color:var(--navy);line-height:1}
.brand .mark{width:7px;height:7px;background:var(--navy)}

/* title slide */
.title-red{position:absolute;inset:0}
.title-photo{position:absolute;left:192px;top:0;width:330px;height:294px;background:linear-gradient(135deg,#ededed 0%,#d9d4cf 45%,#e8a0a8 70%,#cfcfd2 100%)}
.title-box{position:absolute;left:17px;top:43px;width:255px;height:73px;background:var(--navy);border-radius:0 26px 0 0;color:#fff;font-size:27px;font-weight:400;line-height:1.02;padding:8px 0 0 23px}
.s-title .brand{bottom:14px;font-size:7px}

/* diabetes slide */
.panel{position:absolute;background:var(--panel)}
.p-left{left:28px;top:64px;width:152px;height:182px;text-align:center;font-size:8.7px;line-height:1.35;padding:66px 12px 0}
.p-left svg{position:absolute;left:50px;top:8px}
.p-right{left:195px;top:64px;width:301px;height:182px;font-size:8.2px;line-height:1.4}
.p-right svg{position:absolute;left:14px;top:12px}
.avoid{position:absolute;left:64px;top:18px;color:var(--red);font-weight:700;font-size:10.5px}
.p-right ul{position:absolute;left:72px;top:38px;width:222px;list-style:none;text-align:center}
.p-right li{position:relative;margin-bottom:8px}
.p-right li::before{content:"";position:absolute;left:-2px;top:5px;width:3px;height:3px;border-radius:50%;background:var(--red)}
.p-right .sub{font-size:6px;text-align:left;padding-left:14px;margin-top:-2px}
.p-right .sub::before{width:4px;height:4px;border-radius:0;background:none;border-right:1.5px solid var(--red);border-bottom:1.5px solid var(--red);transform:rotate(-45deg);left:3px;top:2px}

/* antipsychotics slide */
.pill-scene{position:absolute;inset:0;background:linear-gradient(120deg,var(--sky) 0%,#a9d3f2 55%,#dbe9f4 100%)}
.s-antipsych .heading{color:#2a2a4a}
.card{position:absolute;top:64px;width:154px;height:182px;background:rgba(255,255,255,.82);text-align:center;color:#3d3d3d}
.card svg{position:absolute;right:12px;top:10px}
.c1{left:15px;font-size:9.5px;line-height:1.35;padding:68px 10px 0}
.c1 strong{color:var(--red)}
.c2{left:185px;font-size:6.7px;line-height:1.3;padding:60px 8px 0}
.c3{left:354px;font-size:11px;line-height:1.2;padding:70px 14px 0}

/* ADR slide */
.chev{position:absolute;left:56px;top:60px}
.band{position:absolute;left:0;right:0;top:88px;height:125px;background:var(--panel)}
.donut{position:absolute;top:10px;width:110px;text-align:center}
.donut span{display:block;font-size:7px;color:#333;margin-top:3px}
.d1{left:70px}.d2{left:206px}.d3{left:343px}
.note{position:absolute;left:42px;top:220px;width:450px;font-size:6.7px;line-height:1.55;color:#555}
</style>
</head>
<body>

<section class="slide s-title">
  <svg class="title-red" width="522" height="294" aria-hidden="true"><polygon points="0,0 38,0 192,294 0,294" fill="#ec1c24"/></svg>
  <div class="title-photo" role="img" aria-label="Photo of a young woman helping an elderly woman sort her pill organiser at a table"></div>
  <h1 class="title-box">Medication<br>Use in Elders.</h1>
  <div class="brand"><i class="mark"></i>Harlow Bureau of Wellness</div>
</section>

<section class="slide s-diabetes">
  <h2 class="heading">Best Drugs in Diabetic Elders</h2>
  <div class="heading-rule"></div>
  <div class="page-no">5</div>
  <div class="panel p-left">
    <svg width="52" height="48" viewBox="0 0 52 48" fill="none" stroke="#9fe0b5" stroke-width="2"><rect x="3" y="6" width="34" height="16" rx="8" transform="rotate(-45 20 14)"/><line x1="14" y1="8" x2="26" y2="20"/><circle cx="36" cy="32" r="12"/><line x1="28" y1="40" x2="44" y2="24"/></svg>
    Only metformin should be used to achieve hemoglobin A1c &lt; 7.5% in most older adults with type 2 diabetes.
  </div>
  <div class="panel p-right">
    <svg width="38" height="40" viewBox="0 0 38 40" fill="none" stroke="#f06f6f" stroke-width="1.8"><line x1="6" y1="2" x2="14" y2="10"/><line x1="10" y1="6" x2="18" y2="14"/><rect x="12" y="12" width="10" height="20" transform="rotate(-45 17 22)"/><line x1="26" y1="28" x2="34" y2="36"/></svg>
    <div class="avoid">AVOID INSULIN!</div>
    <ul>
      <li>Insulin-related hypoglycemia and errors are implicated in an estimated 9.2% of ED visits associated with ADE (Marsh et al 2014).</li>
      <li>This one preventable ADE accounts for nearly 100,000 ED Visits every year.</li>
      <li class="sub">Patients at or above the age of 80 were twice as likely to visit the ED and 5 times more likely to be hospitalized.</li>
    </ul>
  </div>
  <div class="brand"><i class="mark"></i>Harlow Bureau of Wellness</div>
  <div class="footer">www.hlb.example-gov.org</div>
</section>

<section class="slide s-antipsych">
  <div class="pill-scene" role="img" aria-label="Photo of scattered white pills on a light blue surface"></div>
  <h2 class="heading">Antipsychotics</h2>
  <div class="heading-rule"></div>
  <div class="page-no">6</div>
  <div class="card c1">
    <svg width="24" height="26" viewBox="0 0 24 26" fill="#f06f6f"><rect x="4" y="6" width="3.5" height="11" rx="1.7"/><rect x="8.5" y="2" width="3.5" height="14" rx="1.7"/><rect x="13" y="3" width="3.5" height="13" rx="1.7"/><rect x="17.5" y="6" width="3.5" height="11" rx="1.7"/><rect x="4" y="13" width="17" height="12" rx="5"/></svg>
    Antipsychotics should <strong>NOT</strong> be the first choice to treat behavioral and psychological symptoms of dementia.
  </div>
  <div class="card c2">
    <svg width="26" height="24" viewBox="0 0 26 24" fill="#f06f6f"><line x1="2" y1="4" x2="24" y2="22" stroke="#f06f6f" stroke-width="3"/><line x1="24" y1="4" x2="2" y2="22" stroke="#f06f6f" stroke-width="3"/><circle cx="13" cy="11" r="8"/><circle cx="10" cy="11" r="2" fill="#fff"/><circle cx="16" cy="11" r="2" fill="#fff"/></svg>
    Risks of antipsychotics include:<br>- Death<br>- Strokes<br>- Diabetes<br>- Weight gain<br>- Cognitive decline<br>- Neuroleptic malignant syndrome<br>(fever, autonomic instability, altered mental state and extrapyramidal signs)<br>- Extrapyramidal effects<br>- Hypothermia<br>- Oversedation<br>- Falls
  </div>
  <div class="card c3">
    <svg width="24" height="26" viewBox="0 0 24 26" fill="#f06f6f"><path d="M4 24 V17 C1 14 1 7 6 4 C11 0 21 2 22 10 L24 15 L21 15 V19 H16 V24 Z"/><path d="M13 6 L9 13 H13 L11 19 L16 11 H12 Z" fill="#fff"/></svg>
    Antipsychotics may actually increase delirium
  </div>
  <div class="brand"><i class="mark"></i>Harlow Bureau of Wellness</div>
  <div class="footer">www.hlb.example-gov.org</div>
</section>

<section class="slide s-adr">
  <h2 class="heading">Drug Classes Most Commonly Involved in ADRs</h2>
  <div class="heading-rule"></div>
  <div class="page-no">3</div>
  <svg class="chev" width="12" height="16" viewBox="0 0 12 16"><polyline points="2,2 9,8 2,14" fill="none" stroke="#25256b" stroke-width="3"/></svg>
  <div class="band">
    <div class="donut d1">
      <svg width="92" height="92" viewBox="0 0 92 92"><circle cx="46" cy="46" r="40" fill="none" stroke="#d6d6d6" stroke-width="10"/><circle cx="46" cy="46" r="40" fill="none" stroke="#c49a3a" stroke-width="10" stroke-dasharray="85.5 251.3" transform="rotate(-90 46 46)"/><text x="46" y="53" text-anchor="middle" font-family="Lato,sans-serif" font-weight="700" font-size="20" fill="#c49a3a">34%</text></svg>
      <span>Cardiovascular agents</span>
    </div>
    <div class="donut d2">
      <svg width="92" height="92" viewBox="0 0 92 92"><circle cx="46" cy="46" r="40" fill="none" stroke="#d6d6d6" stroke-width="10"/><circle cx="46" cy="46" r="40" fill="none" stroke="#25256b" stroke-width="10" stroke-dasharray="45.2 251.3" transform="rotate(-90 46 46)"/><text x="46" y="53" text-anchor="middle" font-family="Lato,sans-serif" font-weight="700" font-size="20" fill="#25256b">18%</text></svg>
      <span>Analgesic medications</span>
    </div>
    <div class="donut d3">
      <svg width="92" height="92" viewBox="0 0 92 92"><circle cx="46" cy="46" r="40" fill="none" stroke="#d6d6d6" stroke-width="10"/><circle cx="46" cy="46" r="40" fill="none" stroke="#ec1c24" stroke-width="10" stroke-dasharray="25.1 251.3" transform="rotate(-90 46 46)"/><text x="46" y="53" text-anchor="middle" font-family="Lato,sans-serif" font-weight="700" font-size="20" fill="#ec1c24">10%</text></svg>
      <span>Anti-diabetic drugs</span>
    </div>
  </div>
  <p class="note">Predictors of ADRs included the number of medications, use of hypoglycaemic agents, history of hyperlipidaemia, raised white cell count on admission and length of stay. (Okonde 2012)</p>
  <div class="brand"><i class="mark"></i>Harlow Bureau of Wellness</div>
  <div class="footer">&nbsp;</div>
</section>

</body>
</html>
```